Hair Growth Oil - Lustra Crown Drops

Product Label Re-Vamp. we need this label to look more professional and eye-catching label. the one we have nt is ok but not great.

This Formula has 15 different Organic herbs. we'd like to highlight that on the label by showing pictures of most or all of these herbs. i've attached some herbs pics.

This product is our #1 seller and requires the cleanest and most eye-catching look.

This is a hair oil that we make from scratch. each bottle has 34 natural ingredients 15 of which are herbs. i would like a label that shows a lot of herbs on the label that is bright and vibrant.

attached you find our current bottle. and a few examples of herb pictures that i found online.

Things that id like to be included on the label. size will be 4'' wide x 2'' tall

• Concentrated formula
• Promotes thick, long hair growth
• Promotes growth by strengthening and conditioning
• Nourishes the scalp and hair
• Revives dull, damaged or chemically treated hair

No Parabens, No Petroleum, No Mineral Oil, No Artificial Colors

Directions
Shake well before using. Massage a few drops gently into scalp as 2-3 times a week. Do not rinse out. Style as desired.

Made In Harlem NYC
Not Tested on Animals
Store In A Cool Dry Place

Ingredients: Soybean Oil, Olive Fruit Oil, Sweet Almond Oil, Grapeseed Oil, 15 stimulating herb blend, Lemongrass Oil, Peppermint Oil, Tea Tree Oil, Orange Oil, Camphor, Rosemary Oil, Lavender Oil, Cedar Wood Oil & More.

there will also be a barcode on this label.

Please arrange these items on the label the best way you see fit.

Target Market(s)

woman 20-50 years

Industry/Entity Type

Hair

Font styles to use
Script

Colors
ffffff
acd036
fbee3d
fde599
f37122

Requirements
Must have
• White Background.
• herbs within the label ( one pile or many piles)
• clean
• barcode ( it will be provided)
• id also rather the Amber meadow logo verticle.
Nice to have
• icons - not tested on animals, recycle ect
Should not have
• no cartoons charaters

```html
<!DOCTYPE html>
<html lang="en">
<head>
<meta charset="utf-8">
<title>Lustra Crown Drops – Label</title>
<link href="https://fonts.googleapis.com/css2?family=Montserrat:wght@800&family=Open+Sans:wght@400;600;700&display=swap" rel="stylesheet">
<style>
  :root {
    --canvas: #f1f1f1;
    --label: #ffffff;
    --ink: #3c3c3c;
    --ink-soft: #555555;
    --green: #3e9a2c;
    --leaf: #5fb82e;
    --orange: #f37122;
    --herb-gold: #e9a72a;
    --herb-lavender: #8f8cae;
    --herb-chamomile: #d6c25a;
    --rule: #9a9a9a;
  }
  * { margin: 0; padding: 0; box-sizing: border-box; }
  html, body { width: 1200px; height: 1086px; overflow: hidden; background: var(--canvas); }
  body { font-family: "Open Sans", Arial, sans-serif; color: var(--ink); position: relative; }

  .label {
    position: absolute; left: 50px; top: 268px;
    width: 1100px; height: 550px;
    background: var(--label);
    box-shadow: 0 2px 10px rgba(0,0,0,0.08);
  }

  /* Benefits panel */
  .benefits { position: absolute; left: 40px; top: 58px; width: 330px; list-style: none; }
  .benefits li {
    position: relative; padding-left: 22px; margin-bottom: 12px;
    font-size: 16px; line-height: 1.4; color: var(--ink-soft);
  }
  .benefits li svg { position: absolute; left: 0; top: 5px; width: 13px; height: 13px; }

  .free-from { position: absolute; left: 78px; top: 308px; list-style: none; }
  .free-from li { font-size: 19px; line-height: 1.22; color: var(--ink); }
  .free-from li::before { content: "•"; color: var(--leaf); margin-right: 6px; }

  .code-area {
    position: absolute; left: 58px; top: 440px; width: 212px; height: 94px;
    border: 1.5px solid var(--ink-soft);
  }

  /* Front panel */
  .brand-name {
    position: absolute; left: 385px; top: 530px;
    transform: rotate(-90deg); transform-origin: left top;
    font-weight: 700; font-size: 42px; color: var(--orange);
    white-space: nowrap; letter-spacing: 1px;
  }
  .product-title {
    position: absolute; left: 470px; top: 66px;
    font-family: "Montserrat", Arial, sans-serif; font-weight: 800;
    font-size: 44px; line-height: 1.14; color: var(--green);
    letter-spacing: 1px; text-transform: uppercase;
  }
  .herb-pile {
    position: absolute; left: 458px; top: 248px; width: 240px; height: 270px;
    background:
      radial-gradient(ellipse 48% 18% at 50% 14%, var(--herb-gold), transparent 100%),
      radial-gradient(ellipse 46% 17% at 48% 48%, var(--herb-lavender), transparent 100%),
      radial-gradient(ellipse 52% 20% at 52% 82%, var(--herb-chamomile), transparent 100%);
  }

  /* Back panel */
  .info { position: absolute; left: 790px; top: 54px; width: 270px; font-size: 14.5px; line-height: 1.33; color: var(--ink); }
  .info h3 { font-size: 15px; font-weight: 600; }
  .ingredients { margin-top: 28px; }
  .ingredients strong { font-weight: 600; }

  .badges { position: absolute; left: 868px; top: 370px; display: flex; gap: 26px; align-items: center; }
  .badge-square { width: 40px; height: 40px; border: 2px solid var(--ink); border-radius: 6px; }
  .badge-circle { width: 42px; height: 42px; border-radius: 50%; background: var(--ink); }

  .origin { position: absolute; left: 795px; top: 454px; font-size: 15px; color: var(--ink); }
  .storage { position: absolute; left: 795px; top: 492px; font-size: 15px; color: var(--ink); }
</style>
</head>
<body>
  <section class="label">
    <ul class="benefits">
      <li><svg viewBox="0 0 12 12"><path d="M1 11 C2 5 6 2 11 1 C10 6 7 10 1 11Z" fill="var(--leaf)"/></svg>Concentrated formula</li>
      <li><svg viewBox="0 0 12 12"><path d="M1 11 C2 5 6 2 11 1 C10 6 7 10 1 11Z" fill="var(--leaf)"/></svg>Promotes thick, long hair growth</li>
      <li><svg viewBox="0 0 12 12"><path d="M1 11 C2 5 6 2 11 1 C10 6 7 10 1 11Z" fill="var(--leaf)"/></svg>Promotes growth by strengthening and conditioning</li>
      <li><svg viewBox="0 0 12 12"><path d="M1 11 C2 5 6 2 11 1 C10 6 7 10 1 11Z" fill="var(--leaf)"/></svg>Nourishes the scalp and hair</li>
      <li><svg viewBox="0 0 12 12"><path d="M1 11 C2 5 6 2 11 1 C10 6 7 10 1 11Z" fill="var(--leaf)"/></svg>Revives dull, damaged or chemically treated hair</li>
    </ul>

    <ul class="free-from">
      <li>No Parabens,</li>
      <li>No Petroleum</li>
      <li>No Mineral Oil</li>
      <li>No Artificial Colors</li>
    </ul>

    <div class="code-area"></div>

    <div class="brand-name">Amber meadow</div>

    <h1 class="product-title">Lustra<br>Crown<br>Drops</h1>

    <div class="herb-pile" role="img" aria-label="Three piles of dried herbs: calendula petals, lavender buds and chamomile flowers"></div>

    <div class="info">
      <h3>Directions:</h3>
      <p>Shake well before using. Massage a few drops gently into scalp as 2-3 times a week. Do not rinse out. Style as desired.</p>
      <p class="ingredients"><strong>Ingredients:</strong> Soybean Oil, Olive Fruit Oil, Sweet Almond Oil, Grapeseed Oil, 15 stimulating herb blend, Lemongrass Oil, Peppermint Oil, Tea Tree Oil, Orange Oil, Camphor, Rosemary Oil, Lavender Oil, Cedar Wood Oil &amp; More.</p>
    </div>

    <div class="badges">
      <div class="badge-square" role="img" aria-label="Not tested on animals badge"></div>
      <div class="badge-circle" role="img" aria-label="Recycling badge"></div>
    </div>

    <p class="origin">Made In Harlem NYC</p>
    <p class="storage">Store In A Cool Dry Place</p>
  </section>
</body>
</html>
```